Tom & Nia's Homepage Design - Florists

Hello ArtHivePro,

We’re Tom and Nia and we own a lovely flower shop in Marlow. We’re looking to launch a website that gives our customers all information they need to know about getting in contact with us. In time we hope the website will grow and we will want to add new pages as we go along including ecommerce functionality, so the design will need to allow for this.

The brief:
We are looking for 1 homepage design. We have already had our logo designed, which we’ve attached for you to use. At the moment we’re keen to have a homepage design that showcases six of our most popular bouquets, see attached pictures and our contact details. We are looking for a contemporary design that’s inline with our logo. Please do not use dark background colours, we want a clean, light and simple design that looks fresh, modern and professional. Please remember that the majority of web monitors now use a screen resolution of 1366x768. Therefore please do not design a 800 x 600 homepage.

1. Our logo and icon (See attachments)
2. Potential hero images attached for inspiration. 6 Bouquets attached but dont make it look like a bog standard ecommerce site. You dont have to use the 6 bouquets. Our site is more brand as we dont have ecom functionality yet.
3. Our contact details including:

Name:
Tom and Nia’s (note 1 ‘L’ in Nia’s name, use the logo)

Navigation

Homepage needs to include the following copy
‘Free delivery with all orders”
‘Fresh – 7 days of flower freshness guaranteed’
‘Hand delivered and hand prepared by a professional florist’
Very clear call to action to ‘Order today: 0203 574 2261 or email us (visually a clickable link) today

Payment visuals: show that we accept KORVA/Paymoriant/Harbour Quickcard/Zentrip, with logos

Telephone numbers:
0203 574 2261 (Central London)
0208 417 5309 (Greater London)
01628 735142 (Marlow)
07812 906218 (Mobile)

E-mail address
orders@tomandnias.co.uk (Orders)
CS@tomandnias.co.uk (Customer Service)

Chatterly page link (use CH logo)
http://www.facebook.com/tomandnias

The Northfield Petal Guild logo
Attached should be displayed on the bottom of the homepage somewhere, prefer bottom right.

Other sites we like:
http://www.bloomsbygwendra.com
http://maisonvertilune.com
Like the fun of this one - http://www.puddlegoose.co.uk/goto/home

Our logo should be a good guide for how we’d like the overall page to look, please use this as a starter for your designs. Fee; free to submit your designs and I’ll feedback on changes.

We look forward to seeing your designs!

Tom & Nia

Industry/Entity Type

Florist

Requirements
Must have
• Please see the attached brief. Please use our logo and icon in the design.
Should not have
• Do not use dark background colours, it should feel light and fresh.

```html
<!DOCTYPE html>
<html lang="en">
<head>
<meta charset="utf-8">
<title>Tom &amp; Nia's – Florists</title>
<link href="https://fonts.googleapis.com/css2?family=Open+Sans:wght@400;600;700&family=Oswald:wght@500;600&display=swap" rel="stylesheet">
<style>
:root{
  --purple:#7b2f86;--purple-dark:#5e1f6a;--purple-light:#9a4aa6;
  --red:#e0474c;--green:#7cbb3d;--green-dark:#5fa229;
  --ink:#444;--muted:#666;--line:#ddd;--page:#fff;--bg:#f2f2f2;--black:#0d0d0d;
}
*{box-sizing:border-box;margin:0;padding:0}
html,body{width:682px;height:1200px;overflow:hidden}
body{position:relative;background:var(--bg);font-family:"Open Sans",Arial,sans-serif;color:var(--ink);font-size:7px}
.abs{position:absolute}
a{color:inherit;text-decoration:none}
.page{left:39px;top:0;width:604px;height:1003px;background:var(--page)}
.toplinks{right:55px;top:10px;color:var(--red);font-size:7px}
.toplinks span{color:#aaa;margin:0 3px}
.logo{left:48px;top:30px;font-family:"Open Sans",sans-serif;font-weight:700;font-size:25px;color:#333;letter-spacing:-.5px}
.logo-mark{left:66px;top:18px;width:20px;height:20px;border-radius:50%;background:var(--purple)}
.basket{right:40px;top:40px;color:var(--red);font-size:7.5px}
.basket b{font-weight:600;margin-left:5px}
.search{left:486px;top:58px;width:156px;height:16px;background:#f0dede;display:flex}
.search span{flex:1;padding:3px 7px;color:#666;font-size:6.5px}
.search b{width:19px;background:var(--red);color:#fff;font-size:7px;text-align:center;line-height:16px;font-weight:600}
.nav{left:39px;top:81px;width:604px;height:32px;background:linear-gradient(#9a4aa6,#6d2878);display:flex}
.nav a{color:#fff;font-size:7.5px;font-weight:600;padding:0 13px;line-height:32px;border-right:1px solid rgba(255,255,255,.35)}
.nav a:first-child{padding-left:19px}
.hero{left:44px;top:117px;width:420px;height:250px;background:radial-gradient(ellipse at 60% 40%,#e59ac8,#c9d7e8 45%,#7e8c5c 85%)}
.special{left:463px;width:172px;height:80px;background:#fff;border:1px solid #e8e8e8}
.special .pic{left:8px;top:8px;width:66px;height:64px;border:2px solid #eee}
.special h3{left:82px;top:10px;font-family:"Oswald",sans-serif;font-weight:600;font-size:10.5px}
.special p{left:82px;top:25px;width:84px;font-size:6.4px;line-height:9.5px;color:#555}
.special .btn{left:82px;top:61px;padding:0 5px;height:12px;line-height:12px;color:#fff;font-size:5.8px;font-weight:700}
.welcome-title{left:55px;top:380px;font-weight:700;font-size:9.5px;color:var(--purple)}
.lead{left:55px;top:396px;width:395px;font-weight:600;font-size:7px;line-height:10.5px;color:var(--purple)}
.body-copy{left:55px;top:420px;width:395px;font-size:6.6px;line-height:10.5px;color:#444}
.card{width:131px;height:166px;border:1px solid var(--line);background:#fff}
.card .pic{left:6px;top:6px;width:117px;height:110px}
.card .name{left:7px;top:122px;font-size:8.5px;color:#444}
.card .avail{left:7px;top:136px;font-size:6px;color:#555}
.card .price{left:7px;top:148px;font-size:7.5px;color:#333}
.card .price b{color:var(--purple);font-size:10px;font-weight:700}
.box-head{left:463px;width:175px;height:26px;background:linear-gradient(#fff,#ececec);border:1px solid #e2e2e2;font-family:"Oswald",sans-serif;font-weight:500;font-size:10px;color:#555;padding:4px 17px}
.side-list{left:463px;top:397px;width:175px;height:101px;border:1px solid #e2e2e2;border-top:0;list-style:none;padding:6px 0 0 24px}
.side-list li{font-size:6.8px;color:var(--purple);font-weight:600;height:14.8px;position:relative}
.side-list li::before{content:"";position:absolute;left:-6px;top:2.5px;border:2.5px solid transparent;border-left-color:var(--purple)}
.promo{left:463px;width:175px;height:58px;background:linear-gradient(#87c64a,var(--green-dark));color:#fff;padding:14px 12px}
.promo h4{font-size:9px;font-weight:700;line-height:11px}
.promo p{font-size:8px;font-weight:600;line-height:11.5px}
.promo svg{position:absolute;right:12px;top:10px}
.order{left:463px;top:685px;width:175px;height:86px;background:linear-gradient(#8f3e9b,var(--purple-dark));color:#fff;padding:10px 17px}
.order h4{font-family:"Oswald",sans-serif;font-weight:500;font-size:11px}
.order .phone{font-size:13px;line-height:16px}
.order p{font-size:7.5px}
.order .cta{display:inline-block;margin-top:6px;background:#2e0f33;font-size:6.5px;font-weight:700;padding:3px 6px;border-radius:2px}
.types{left:463px;top:801px;width:175px;height:180px;border:1px solid #e2e2e2;border-top:0;display:flex;padding:13px 0 0 18px}
.types ul{list-style:none;width:74px}
.types li{font-size:6.6px;font-weight:600;color:#444;height:14.8px}
.foot-col{top:1017px;border-right:1px solid #ccc;height:120px}
.foot-col h5{font-weight:400;font-size:9px;color:#555;margin-bottom:8px}
.foot-col ul{list-style:none}
.foot-col li{font-size:6.6px;color:#444;height:13px}
.pay{top:1038px;width:38px;height:20px;border-radius:2px;color:#fff;font-size:5px;font-weight:700;display:flex;align-items:center;justify-content:center;text-align:center;line-height:6px}
.social{top:1092px;width:18px;height:18px;border-radius:50%}
.bottom{left:0;top:1164px;width:682px;height:36px;background:var(--black);color:#ddd;font-size:6.4px;padding:13px 47px}
.bottom span{margin:0 4px}
</style>
</head>
<body>
<div class="abs page"></div>

<header>
  <div class="abs toplinks"><a>login</a><span>|</span><a>register</a><span>|</span><a>Contact</a><span>|</span><a>Support</a></div>
  <div class="abs logo-mark"></div>
  <div class="abs logo">Tom &amp; Nia's</div>
  <div class="abs basket">Shopping Basket <b>€0.00</b> <b>0 itmes</b></div>
  <div class="abs search"><span>product search</span><b>Go</b></div>
  <nav class="abs nav"><a>CLASSIC FLOWERS</a><a>LUXURY BOUQUETS</a><a>PLATINUM COLLECTION</a><a>AUTUMN FLOWERS</a><a>LUXURY ROSES</a></nav>
</header>

<div class="abs hero" role="img" aria-label="Pink cosmos flowers in a meadow under a pale sky"></div>

<div class="abs special" style="top:120px">
  <div class="abs pic" role="img" aria-label="Red, pink and white gerbera bouquet" style="background:linear-gradient(135deg,#d23a4a,#e9a6b8,#3c5b2c)"></div>
  <h3 class="abs" style="color:var(--green-dark)">BIRTHDAY SPECIAL</h3>
  <p class="abs">Pellentesque habitant morbi tristique senectus et netus et malesuada</p>
  <a class="abs btn" style="background:var(--green-dark)">VIEW MORE</a>
</div>
<div class="abs special" style="top:202px">
  <div class="abs pic" role="img" aria-label="Pink roses in a glass cube vase" style="background:linear-gradient(135deg,#e2406f,#f07aa0,#b9c3c5)"></div>
  <h3 class="abs" style="color:var(--red)">LOVING SPECIALS</h3>
  <p class="abs">Pellentesque habitant morbi tristique senectus et netus et malesuada</p>
  <a class="abs btn" style="background:var(--red)">VIEW MORE</a>
</div>
<div class="abs special" style="top:284px">
  <div class="abs pic" role="img" aria-label="Purple and white autumn flower arrangement" style="background:linear-gradient(135deg,#8a3c8e,#e3d8e5,#b2486e)"></div>
  <h3 class="abs" style="color:var(--purple)">AUBURN FALL</h3>
  <p class="abs">Pellentesque habitant morbi tristique senectus et netus et malesuada</p>
  <a class="abs btn" style="background:var(--purple)">VIEW MORE</a>
</div>

<main>
  <h1 class="abs welcome-title">WELCOME TO OUR WEBSITE MAINPAGE</h1>
  <p class="abs lead">Pellentesque habitant morbi tristique senectus et netus et malesuada fames ac turpis egestas. In posuere felis nec tortor. Pellentesque faucibus. Ut accumsan ultricies elit.</p>
  <p class="abs body-copy">Pellentesque habitant morbi tristique senectus et netus et malesuada fames ac turpis egestas. Cras id elit. Integer quis urna. Ut ante enim, dapibus malesuada, fringilla eu, condimentum quis, tellus. Aenean porttitor eros vel dolor. Donec convallis pede venenatis nibh. Duis quam.  Aliquam erat volutpat. Quisque dignissim congue leo.</p>

  <div class="abs card" style="left:49px;top:469px"><div class="abs pic" role="img" aria-label="Calla lily bouquet wrapped in hessian" style="background:linear-gradient(160deg,#5b4a3b,#c9b8a6,#8c6d4f)"></div><div class="abs name">Flower Name</div><div class="abs avail">Available for delivery today</div><div class="abs price">From <b>£26.50</b></div></div>
  <div class="abs card" style="left:187px;top:469px"><div class="abs pic" role="img" aria-label="Lilac roses in a vintage basket" style="background:linear-gradient(160deg,#3f3a33,#a893b0,#5d6a4a)"></div><div class="abs name">Flower Name</div><div class="abs avail">Available for delivery today</div><div class="abs price">From <b>£26.50</b></div></div>
  <div class="abs card" style="left:325px;top:469px"><div class="abs pic" role="img" aria-label="Heart shaped flower wreath" style="background:radial-gradient(circle,#d9d2c8,#7b8a5a 60%,#4c5a3a)"></div><div class="abs name">Flower Name</div><div class="abs avail">Available for delivery today</div><div class="abs price">From <b>£26.50</b></div></div>

  <div class="abs card" style="left:49px;top:644px"><div class="abs pic" role="img" aria-label="Pastel bouquet with lavender and peach roses" style="background:linear-gradient(160deg,#b8a6c9,#f1d6c8,#7a6a50)"></div><div class="abs name">Flower Name</div><div class="abs avail">Available for delivery today</div><div class="abs price">From <b>£26.50</b></div></div>
  <div class="abs card" style="left:187px;top:644px"><div class="abs pic" role="img" aria-label="Bright pink and coral peony bouquet" style="background:linear-gradient(160deg,#d8306a,#f29a88,#7a5a40)"></div><div class="abs name">Flower Name</div><div class="abs avail">Available for delivery today</div><div class="abs price">From <b>£26.50</b></div></div>
  <div class="abs card" style="left:325px;top:644px"><div class="abs pic" role="img" aria-label="Red and orange rose bouquet" style="background:radial-gradient(circle,#e0461f,#b31a14 60%,#f3eeee)"></div><div class="abs name">Flower Name</div><div class="abs avail">Available for delivery today</div><div class="abs price">From <b>£26.50</b></div></div>

  <div class="abs card" style="left:49px;top:818px"><div class="abs pic" role="img" aria-label="Soft pink rose and sweet pea arrangement" style="background:linear-gradient(160deg,#5f7a55,#f0c9c8,#8a6b48)"></div><div class="abs name">Flower Name</div><div class="abs avail">Available for delivery today</div><div class="abs price">From <b>£26.50</b></div></div>
  <div class="abs card" style="left:187px;top:818px"><div class="abs pic" role="img" aria-label="Blue grape hyacinth bunch" style="background:linear-gradient(160deg,#e8ece4,#3f4f96,#6d7f4a)"></div><div class="abs name">Flower Name</div><div class="abs avail">Available for delivery today</div><div class="abs price">From <b>£26.50</b></div></div>
  <div class="abs card" style="left:325px;top:818px"><div class="abs pic" role="img" aria-label="Lily of the valley stems on a leaf" style="background:linear-gradient(170deg,#e8e8e6 45%,#6f9a3f)"></div><div class="abs name">Flower Name</div><div class="abs avail">Available for delivery today</div><div class="abs price">From <b>£26.50</b></div></div>
</main>

<aside>
  <div class="abs box-head" style="top:372px">SIDE BAR</div>
  <ul class="abs side-list"><li>Latest Designs</li><li>Our Favourites</li><li>Delivery Information</li><li>Customer Services</li><li>FAQ</li><li>About Us</li></ul>

  <div class="abs promo" style="top:503px"><h4>Fresh Delivery</h4><p>With All Orders</p>
    <svg width="50" height="38" viewBox="0 0 50 38" fill="rgba(255,255,255,.55)"><rect x="0" y="4" width="30" height="24" rx="2"/><path d="M31 11h10l8 9v8H31z"/><circle cx="10" cy="31" r="5"/><circle cx="40" cy="31" r="5"/></svg></div>
  <div class="abs promo" style="top:563px"><h4>Fresh- 7 Days of</h4><p>Flower Freshness<br>Guaranteed</p>
    <svg width="34" height="46" viewBox="0 0 34 46" fill="rgba(255,255,255,.55)"><path d="M17 0c9 0 12 10 6 17 8-3 13 5 9 11-4 5-10 4-13 0l-1 18h-2l-1-18c-3 4-9 5-13 0-4-6 1-14 9-11C5 10 8 0 17 0z"/></svg></div>
  <div class="abs promo" style="top:625px"><h4>Hand Delivered</h4><p>and hand prepared<br>by a Professional florist</p>
    <svg width="32" height="34" viewBox="0 0 32 34" fill="rgba(255,255,255,.55)"><path d="M0 14h7v20H0zM9 14l7-12c3-1 5 1 4 5l-2 6h11c3 0 4 3 3 5l-4 14c-1 2-2 2-4 2H9z"/></svg></div>
  <div class="abs order"><h4>ORDER TODAY:</h4><div class="phone">0203 574 2261</div><p>or Email us Now</p><a class="cta">CLICK HERE NOW</a>
    <svg class="abs" style="right:14px;top:12px" width="40" height="42" viewBox="0 0 40 42" fill="none" stroke="rgba(255,255,255,.6)" stroke-width="2"><path d="M26 2c3 0 6 3 6 5l-4 5 5 12 5 1c1 3-1 7-4 8-8-4-12-14-11-27z"/><path d="M2 24l22-6 4 14-22 6z"/><path d="M2 24l15 5 7-11"/></svg></div>

  <div class="abs box-head" style="top:775px">BY TYPE &amp; OCCASIONS</div>
  <div class="abs types">
    <ul><li>Birthday</li><li>Romantic</li><li>Autumn</li><li>Thank You</li><li>Get Well</li><li>New Baby</li><li>Funeral</li><li>Sympathy</li><li>Other</li></ul>
    <ul><li>All Our Flowers</li><li>Bouquets</li><li>Aquapacks</li><li>Arrangements</li><li>Baskets</li><li>Rose Bouquets</li><li>Hampers</li><li>Baby Gift Sets</li><li>Gift Experience Days</li></ul>
  </div>
</aside>

<footer>
  <div class="abs foot-col" style="left:48px;width:73px"><h5>Occasions</h5><ul><li>New Year</li><li>Diwali</li><li>Birthday</li><li>Wedding Specials</li><li>Mother's Day</li><li>Father's Day</li><li>Valentine's Day</li><li>Spring</li></ul></div>
  <div class="abs foot-col" style="left:143px;width:73px"><h5>Categories</h5><ul><li>All Our Flowers</li><li>Bouquets</li><li>Aquapacks</li><li>Arrangements</li><li>Baskets</li><li>Rose Bouquets</li><li>Hampers</li><li>Baby Gift Sets</li></ul></div>
  <div class="abs foot-col" style="left:240px;width:61px"><h5>Company</h5><ul><li>About Us</li><li>Contact Us</li><li>Help</li><li>Affiliates</li><li>Membership</li><li>Newsletter</li><li>RSS Feed</li></ul></div>
  <div class="abs foot-col" style="left:322px;width:86px"><h5>Support</h5><ul><li>Charity Information</li><li>Our Boxes</li><li>Flower Care Tips</li><li>Delivery Information</li><li>Customer Service</li><li>FAQ</li><li>Site Map</li></ul></div>
  <div class="abs" style="left:430px;top:1017px;font-size:9px;color:#555">Payment Methods</div>
  <div class="abs pay" style="left:430px;background:#1c3f94">KORVA</div>
  <div class="abs pay" style="left:470px;background:#2a7cc0">Harbour Quickcard</div>
  <div class="abs pay" style="left:510px;background:#e0602a">Paymoriant</div>
  <div class="abs pay" style="left:548px;background:#3b5fa8">Cardelle</div>
  <div class="abs" style="left:432px;top:1076px;font-size:7.5px;font-style:italic;color:#555">Connect With Us</div>
  <div class="abs social" role="img" aria-label="Chatterly" style="left:433px;background:#3b5998"></div>
  <div class="abs social" role="img" aria-label="Chirpline" style="left:458px;background:#2aa8e0"></div>
  <div class="abs social" role="img" aria-label="Reelcast" style="left:483px;background:#c4302b"></div>
  <div class="abs social" role="img" aria-label="Linkwork" style="left:508px;background:#0e76a8"></div>
  <div class="abs social" role="img" aria-label="RSS feed" style="left:533px;background:#f26522"></div>
  <div class="abs bottom">© Company Name<span>|</span>Term of Use<span>|</span>Privacy Policy</div>
</footer>
</body>
</html>
```